Value-added components of an energy-as-a-service provider

FolwenTide (www.folwentide.example) is a turnkey energy solutions provider for educational institutions—which essentially means we can make recommendations for ways to improve heating, cooling, ventilation, lighting, building controls, etc., and then turn around and project-manage the implementation of these recommendations.Part of what makes us different than our competitors is recognizing the unique way that educational institutions make decisions: they employ a more collaborative approach, and given the 24/7 nature of school operations, any construction needs to be very carefully planned and communicated with building occupants.We are looking at competing in the "energy-as-a-service" (EaaS) field, which effectively capitalizes on the way institutions can self-supply energy. The biggest hurdles for most projects that either produce or conserve energy are (1) upfront cost (these projects are really expensive) and (2) implementation (full-time employees on campuses already have too much on their plates). What EaaS providers can do is alleviate these burdens by finding the capital to pay for equipment, which the school then repays through the associated energy savings. Providers also do the work of implementing the changes.FolwenTide offers the same basic characteristics that other EaaS providers offer—but we have a few elements that are like the icing on the cake, or the cherry on top (insert your own dessert metaphor here). Namely, we work exclusively with schools and are familiar with that environment, know how to work around sensitive scheduling constraints, know how to engage stakeholders in an academic environment, etc. That's what we would like help with in a graphic. There's a couple of renderings we did in-house, but the feedback on the less crude one attached is that there's a bit too much emphasis on the three differentiating elements, and that it could be a bit more visually appealing. We're really open to suggestions here, but keeping it simple and classy is still paramount. Attached is the FolwenTide brand standards guidebook, which has our color palette and fonts and such, and a couple of iterations of our logo are also attached.
Look and feel
Each slider illustrates characteristics of the customer's brand and the style your logo design should communicate.

```html
<!DOCTYPE html>
<html lang="en">
<head>
<meta charset="utf-8">
<title>FolwenTide – Value-Added Components</title>
<link href="https://fonts.googleapis.com/css2?family=Questrial&display=swap" rel="stylesheet">
<style>
  :root {
    --teal: #4d7a86;
    --navy: #1c3f77;
    --orange: #d06329;
    --brown: #736259;
    --green: #65b946;
    --stone: #8b8987;
    --amber: #f7a51d;
    --pill: #e7e7e7;
    --ring: #c4c4c4;
    --label: #4a4a4a;
    --brand: #6cb33f;
    --paper: #ffffff;
  }
  html, body {
    margin: 0;
    width: 1200px;
    height: 911px;
    overflow: hidden;
    background: var(--paper);
  }
  .components-diagram {
    display: block;
    width: 1200px;
    height: 911px;
  }
  .pill { fill: var(--pill); filter: url(#pillShadow); }
  .label {
    font-family: "Questrial", sans-serif;
    font-size: 38px;
    fill: var(--label);
    letter-spacing: 0.5px;
  }
  .brand-name {
    font-family: "Questrial", sans-serif;
    font-size: 46px;
    fill: var(--brand);
  }
  .stem { stroke-width: 14; stroke-linecap: round; fill: none; }
</style>
</head>
<body>
<svg class="components-diagram" viewBox="0 0 1850 1404" xmlns="http://www.w3.org/2000/svg" role="img" aria-label="FolwenTide value-added energy-as-a-service components">
  <defs>
    <filter id="pillShadow" x="-5%" y="-20%" width="110%" height="150%">
      <feDropShadow dx="0" dy="3" stdDeviation="3" flood-color="#000" flood-opacity="0.18"/>
    </filter>
    <radialGradient id="hubRing" cx="50%" cy="40%" r="60%">
      <stop offset="0%" stop-color="#e2e2e2"/>
      <stop offset="100%" stop-color="#b9b9b9"/>
    </radialGradient>
    <radialGradient id="hubFace" cx="45%" cy="35%" r="70%">
      <stop offset="0%" stop-color="#fafafa"/>
      <stop offset="100%" stop-color="#e8e8e8"/>
    </radialGradient>
  </defs>

  <!-- label pills -->
  <g class="pills">
    <rect class="pill" x="290" y="276" width="470" height="120" rx="60"/>
    <rect class="pill" x="1085" y="276" width="467" height="120" rx="60"/>
    <rect class="pill" x="1245" y="515" width="465" height="120" rx="60"/>
    <rect class="pill" x="113" y="637" width="467" height="120" rx="60"/>
    <rect class="pill" x="1245" y="778" width="473" height="120" rx="60"/>
    <rect class="pill" x="268" y="1010" width="492" height="120" rx="60"/>
    <rect class="pill" x="1085" y="1010" width="490" height="120" rx="60"/>
  </g>

  <!-- stems -->
  <g class="stems">
    <line class="stem" stroke="var(--teal)" x1="725" y1="385" x2="793" y2="475"/>
    <line class="stem" stroke="var(--navy)" x1="1117" y1="385" x2="1048" y2="475"/>
    <line class="stem" stroke="var(--orange)" x1="1250" y1="592" x2="1163" y2="613"/>
    <line class="stem" stroke="var(--brown)" x1="575" y1="695" x2="662" y2="695"/>
    <line class="stem" stroke="var(--green)" x1="1250" y1="818" x2="1163" y2="795"/>
    <line class="stem" stroke="var(--stone)" x1="725" y1="1020" x2="793" y2="938"/>
    <line class="stem" stroke="var(--amber)" x1="1117" y1="1020" x2="1048" y2="938"/>
  </g>

  <!-- outer ring -->
  <circle cx="920" cy="703" r="275" fill="#d6d6d6"/>
  <circle cx="920" cy="703" r="262" fill="#ececec"/>

  <!-- segments -->
  <g class="segments">
    <path fill="var(--navy)" d="M920 458 A245 245 0 0 1 1093.2 529.8 L1029.6 593.4 A155 155 0 0 0 920 548 Z"/>
    <path fill="var(--orange)" d="M1093.2 529.8 A245 245 0 0 1 1165 703 L1075 703 A155 155 0 0 0 1029.6 593.4 Z"/>
    <path fill="var(--green)" d="M1165 703 A245 245 0 0 1 1093.2 876.2 L1029.6 812.6 A155 155 0 0 0 1075 703 Z"/>
    <path fill="var(--amber)" d="M1093.2 876.2 A245 245 0 0 1 920 948 L920 858 A155 155 0 0 0 1029.6 812.6 Z"/>
    <path fill="var(--stone)" d="M920 948 A245 245 0 0 1 707.8 825.5 L785.8 780.5 A155 155 0 0 0 920 858 Z"/>
    <path fill="var(--brown)" d="M707.8 825.5 A245 245 0 0 1 707.8 580.5 L785.8 625.5 A155 155 0 0 0 785.8 780.5 Z"/>
    <path fill="var(--teal)" d="M707.8 580.5 A245 245 0 0 1 920 458 L920 548 A155 155 0 0 0 785.8 625.5 Z"/>
  </g>

  <!-- hub -->
  <circle cx="920" cy="703" r="157" fill="url(#hubRing)"/>
  <circle cx="920" cy="703" r="126" fill="url(#hubFace)"/>
  <text class="brand-name" x="920" y="718" text-anchor="middle">FolwenTide</text>

  <!-- ring nodes -->
  <g class="nodes">
    <g fill="#fff" stroke="#cfcfcf" stroke-width="3">
      <circle cx="793" cy="475" r="27"/>
      <circle cx="1048" cy="475" r="27"/>
      <circle cx="1163" cy="613" r="27"/>
      <circle cx="662" cy="695" r="27"/>
      <circle cx="1163" cy="795" r="27"/>
      <circle cx="793" cy="938" r="27"/>
      <circle cx="1048" cy="938" r="27"/>
    </g>
    <circle cx="793" cy="475" r="12" fill="var(--teal)"/>
    <circle cx="1048" cy="475" r="12" fill="var(--navy)"/>
    <circle cx="1163" cy="613" r="12" fill="var(--orange)"/>
    <circle cx="662" cy="695" r="12" fill="var(--brown)"/>
    <circle cx="1163" cy="795" r="12" fill="var(--green)"/>
    <circle cx="793" cy="938" r="12" fill="var(--stone)"/>
    <circle cx="1048" cy="938" r="12" fill="var(--amber)"/>
  </g>

  <!-- badge circles -->
  <g class="badges">
    <g>
      <circle cx="693" cy="333" r="67" fill="var(--teal)"/>
      <circle cx="693" cy="333" r="57" fill="#fff"/>
      <circle cx="693" cy="333" r="48" fill="var(--teal)"/>
    </g>
    <g>
      <circle cx="1149" cy="333" r="67" fill="var(--navy)"/>
      <circle cx="1149" cy="333" r="57" fill="#fff"/>
      <circle cx="1149" cy="333" r="48" fill="var(--navy)"/>
    </g>
    <g>
      <circle cx="1308" cy="572" r="67" fill="var(--orange)"/>
      <circle cx="1308" cy="572" r="57" fill="#fff"/>
      <circle cx="1308" cy="572" r="48" fill="var(--orange)"/>
    </g>
    <g>
      <circle cx="511" cy="697" r="67" fill="var(--brown)"/>
      <circle cx="511" cy="697" r="57" fill="#fff"/>
      <circle cx="511" cy="697" r="48" fill="var(--brown)"/>
    </g>
    <g>
      <circle cx="1308" cy="838" r="67" fill="var(--green)"/>
      <circle cx="1308" cy="838" r="57" fill="#fff"/>
      <circle cx="1308" cy="838" r="48" fill="var(--green)"/>
    </g>
    <g>
      <circle cx="693" cy="1072" r="67" fill="var(--stone)"/>
      <circle cx="693" cy="1072" r="57" fill="#fff"/>
      <circle cx="693" cy="1072" r="48" fill="var(--stone)"/>
    </g>
    <g>
      <circle cx="1149" cy="1072" r="67" fill="var(--amber)"/>
      <circle cx="1149" cy="1072" r="57" fill="#fff"/>
      <circle cx="1149" cy="1072" r="48" fill="var(--amber)"/>
    </g>
  </g>

  <!-- labels -->
  <g class="labels">
    <text class="label" x="467" y="328" text-anchor="middle">STAKEHOLDER</text>
    <text class="label" x="467" y="369" text-anchor="middle">ENGAGEMENT</text>
    <text class="label" x="1245" y="349">FINANCING</text>
    <text class="label" x="1398" y="588">ENGINEERING</text>
    <text class="label" x="291" y="690" text-anchor="middle">ACADEMIC</text>
    <text class="label" x="291" y="731" text-anchor="middle">INTEGRATION</text>
    <text class="label" x="1395" y="853">CONSTRUCTION</text>
    <text class="label" x="457" y="1066" text-anchor="middle">PEOPLE-CENTRIC</text>
    <text class="label" x="457" y="1107" text-anchor="middle">CONSTRUCTION</text>
    <text class="label" x="1348" y="1086" text-anchor="middle">O &amp; M</text>
  </g>
</svg>
</body>
</html>
```